Modern business card design for professional copywriter

I'd like a business card design that I can use to have my cards printed out by plink.com as a squared corners business card (see artwork and design guidelines here: https://help.plink.com/hc/en-gb/sections/300481726-PLINK-Product-Templates)

The design should be clean and modern and reflect the colours, tone and branding on my website: https://noravestrel.com.au

Target Market(s)

Professionals, B2B small business owners

Industry/Entity Type

Business

Contact Information for Business Card

Nora Vestrel
m: 0427 593 864
e: nora@noravestrel.com.au
w: noravestrel.com.au

Font styles to use
Sans Serif

Requirements
Must have
• Tagline: "Smart copywriting for clever business people"
• Brand colours: fd8000, 009984, 666666 and black
Nice to have

```html
<!DOCTYPE html>
<html lang="en">
<head>
<meta charset="utf-8">
<title>Nora Vestrel – Business Card</title>
<link rel="stylesheet" href="https://fonts.googleapis.com/css2?family=Poppins:wght@400;500;600;700&display=swap">
<style>
  :root {
    --teal: #179c84;
    --teal-dark: #009984;
    --orange: #fd8000;
    --grey: #666666;
    --ink: #111111;
    --paper: #ffffff;
    --backdrop: #e9ecec;
  }
  * { box-sizing: border-box; margin: 0; padding: 0; }
  html, body { width: 1200px; height: 800px; overflow: hidden; }
  body {
    background: var(--backdrop);
    font-family: "Poppins", sans-serif;
    display: flex;
    flex-direction: column;
    align-items: center;
    justify-content: center;
    gap: 40px;
  }
  .card {
    position: relative;
    width: 600px;
    height: 343px;
    background: var(--paper);
    overflow: hidden;
    box-shadow: 0 6px 20px rgba(0,0,0,0.15);
  }

  /* Front side */
  .card-front .front-art { position: absolute; inset: 0; width: 100%; height: 100%; }
  .front-brand {
    position: absolute;
    left: 0; right: 0;
    top: 102px;
    text-align: center;
    color: var(--paper);
    font-weight: 600;
    font-size: 40px;
    letter-spacing: 0.5px;
    transform: rotate(-16.7deg);
  }
  .tagline {
    position: absolute;
    left: 190px;
    top: 280px;
    color: var(--teal-dark);
    font-weight: 600;
    font-size: 11.5px;
    line-height: 1;
    letter-spacing: 0.4px;
    text-transform: uppercase;
    white-space: nowrap;
    transform-origin: left top;
    transform: rotate(-16.7deg);
  }

  /* Back side */
  .edge-bar { position: absolute; width: 7px; }
  .edge-bar-left { left: 0; top: 196px; height: 80px; background: var(--teal); }
  .edge-bar-right { right: 0; top: 44px; height: 80px; background: var(--orange); }

  .person {
    position: absolute;
    right: 52px;
    top: 44px;
    text-align: right;
  }
  .person-name {
    color: var(--teal);
    font-weight: 700;
    font-size: 24px;
    letter-spacing: 1.5px;
    line-height: 1;
  }
  .person-role {
    color: var(--ink);
    font-size: 15px;
    line-height: 1.2;
  }
  .rule { position: absolute; height: 2px; }
  .rule-orange { right: 52px; top: 112px; width: 180px; background: var(--orange); }
  .rule-teal { right: 52px; top: 124px; width: 220px; background: var(--teal); }

  .back-brand {
    position: absolute;
    left: 48px;
    top: 214px;
    display: flex;
    align-items: center;
    gap: 10px;
    color: var(--teal);
    font-weight: 600;
    font-size: 28px;
  }
  .back-brand .mark {
    width: 14px; height: 14px;
    border-radius: 50%;
    background: var(--orange);
  }

  .contacts {
    position: absolute;
    right: 24px;
    bottom: 40px;
    list-style: none;
    text-align: right;
    color: var(--ink);
    font-size: 17px;
    line-height: 1.55;
  }
  .contacts li { display: flex; align-items: center; justify-content: flex-end; gap: 10px; }
  .contacts .icon { width: 22px; height: 22px; flex: none; }
</style>
</head>
<body>

  <section class="card card-front" aria-label="Business card front">
    <svg class="front-art" viewBox="0 0 600 343" preserveAspectRatio="none" aria-hidden="true">
      <rect width="600" height="343" fill="#179c84"/>
      <polygon points="0,343 600,343 600,150 0,330" fill="#ffffff"/>
    </svg>
    <div class="front-brand">Nora Vestrel</div>
    <p class="tagline">Smart copywriting for clever business people</p>
  </section>

  <section class="card card-back" aria-label="Business card back">
    <span class="edge-bar edge-bar-left"></span>
    <span class="edge-bar edge-bar-right"></span>

    <div class="person">
      <h1 class="person-name">NORA VESTREL</h1>
      <p class="person-role">Copywriter</p>
    </div>
    <span class="rule rule-orange"></span>
    <span class="rule rule-teal"></span>

    <div class="back-brand"><span class="mark"></span>Nora Vestrel</div>

    <ul class="contacts">
      <li>0427 593 864
        <svg class="icon" viewBox="0 0 24 24" aria-hidden="true">
          <rect x="6" y="2" width="12" height="20" rx="2.5" fill="none" stroke="#179c84" stroke-width="2"/>
          <circle cx="12" cy="18.5" r="1" fill="#179c84"/>
        </svg>
      </li>
      <li>nora@noravestrel.com.au
        <svg class="icon" viewBox="0 0 24 24" aria-hidden="true">
          <rect x="2" y="6" width="20" height="13" fill="#fd8000"/>
          <polyline points="2,6 12,13 22,6" fill="none" stroke="#ffffff" stroke-width="1.5"/>
        </svg>
      </li>
      <li>noravestrel.com.au
        <svg class="icon" viewBox="0 0 24 24" aria-hidden="true">
          <circle cx="12" cy="12" r="10" fill="#179c84"/>
          <g fill="none" stroke="#ffffff" stroke-width="1.2">
            <ellipse cx="12" cy="12" rx="4.5" ry="10"/>
            <line x1="2" y1="12" x2="22" y2="12"/>
            <line x1="12" y1="2" x2="12" y2="22"/>
            <path d="M4 7h16M4 17h16"/>
          </g>
        </svg>
      </li>
    </ul>
  </section>

</body>
</html>
```